Property refurbishment & maintenance Business Card Design

Velkoran Ltd is a leading provider of domestic maintenance, building and refurbishment services. Founded in October 2009 by Milo Velkoran, we aim to provide our customers with exceptional home improvement and maintenance services whilst minimising the disruption and stress caused.
The building services we provide are of the very highest quality. We provide all of your customers with the peace of mind in knowing that they are dealing with experts in construction, renovation and decoration. This is because we are members of the Guild of Certified Tradecrafters (GCT). We have also had our credentials verified by Pledgeline and the UK government's Fair Seal scheme.
Target Market(s)
Private home owners,letting agents,tenants
Industry/Entity Type
Home Improvement
Contact Information for Business Card
Velkoran ltd.
Milo Velkoran
18 Brindle Cope Lane ,Waltham Cross,Herts,EN4 2QW,T.01632960517 M:07700900382
E. info@velkoran.co.uk. www.velkoran.co.uk

```html
<!DOCTYPE html>
<html lang="en">
<head>
<meta charset="utf-8">
<title>Velkoran Ltd – Business Card</title>
<link href="https://fonts.googleapis.com/css2?family=Open+Sans:wght@400;600;700&display=swap" rel="stylesheet">
<style>
  :root {
    --backdrop: #ece9e4;
    --card: #ffffff;
    --teal: #3a9e8a;
    --gold: #c48a3a;
    --charcoal: #555657;
    --ink: #3d3d3d;
    --light: #ffffff;
  }
  * { margin: 0; padding: 0; box-sizing: border-box; }
  html, body {
    width: 1200px; height: 1193px; overflow: hidden;
    background: var(--backdrop);
    font-family: "Open Sans", Arial, sans-serif;
  }
  .canvas { position: relative; width: 1200px; height: 1193px; }
  .card {
    position: absolute; width: 917px; height: 521px;
    background: var(--card); border-radius: 30px; overflow: hidden;
    box-shadow: 0 6px 18px rgba(0,0,0,0.18);
  }
  .card--front { left: 30px; top: 58px; }
  .card--back { left: 220px; top: 619px; }

  .brand-name {
    position: absolute; color: var(--teal); font-weight: 400;
    letter-spacing: 6px; line-height: 1; white-space: nowrap;
  }
  .card--front .brand-name { left: 88px; top: 108px; font-size: 64px; }
  .card--back .brand-name { left: 0; width: 100%; text-align: center; top: 200px; font-size: 78px; }

  .holder {
    position: absolute; left: 91px; top: 222px;
    font-size: 27px; font-weight: 700; color: var(--ink);
  }
  .holder .title { font-weight: 400; color: var(--gold); font-size: 22px; }

  .wave { position: absolute; left: 0; top: 0; width: 917px; height: 521px; }

  .contact-list { position: absolute; left: 72px; top: 372px; list-style: none; }
  .contact-list li {
    display: flex; align-items: center; height: 34px;
    color: var(--light); font-size: 21px;
  }
  .contact-list svg { width: 22px; height: 22px; margin-right: 14px; flex: none; }

  .divider {
    position: absolute; left: 367px; top: 436px; width: 2px; height: 70px;
    background: var(--light); opacity: 0.85;
  }
  .address {
    position: absolute; left: 392px; top: 442px;
    color: var(--light); font-size: 21px; line-height: 32px; font-style: normal;
  }

  .web {
    position: absolute; left: 0; width: 100%; top: 380px; text-align: center;
    font-size: 29px; letter-spacing: 3px; color: var(--ink);
  }
</style>
</head>
<body>
<main class="canvas">

  <section class="card card--front" aria-label="Business card front">
    <svg class="wave" viewBox="0 0 917 521" aria-hidden="true">
      <path fill="var(--gold)" d="M0,286 C200,246 380,282 560,346 C700,392 820,384 917,342 L917,356 C820,398 700,408 560,364 C380,302 200,270 0,310 Z"/>
      <path fill="var(--charcoal)" d="M0,334 C200,300 380,330 560,392 C700,436 820,420 917,380 L917,521 L0,521 Z"/>
    </svg>

    <div class="brand-name">VELKORAN</div>
    <p class="holder">Your Name, <span class="title">Title</span></p>

    <ul class="contact-list">
      <li>
        <svg viewBox="0 0 24 24" aria-hidden="true"><circle cx="12" cy="12" r="11" fill="var(--light)"/><path d="M8 6c1 0 2 2.5 2 3s-1 1-1 1.5 2 3.5 3.5 4c.5 0 1-1 1.5-1s3 1 3 2-1.5 2.5-2.5 2.5C10 18 6 13 6 8.5 6 7 7 6 8 6z" fill="var(--charcoal)"/></svg>
        01632960517
      </li>
      <li>
        <svg viewBox="0 0 24 24" aria-hidden="true"><rect x="7" y="3" width="10" height="18" rx="2" fill="var(--light)"/><rect x="9" y="6" width="6" height="8" fill="var(--charcoal)"/><circle cx="12" cy="17.5" r="1.2" fill="var(--charcoal)"/></svg>
        07700900382
      </li>
      <li>
        <svg viewBox="0 0 24 24" aria-hidden="true"><circle cx="12" cy="12" r="11" fill="var(--light)"/><rect x="6" y="8" width="12" height="8" rx="1" fill="var(--charcoal)"/><path d="M6.5 8.5 12 13l5.5-4.5" stroke="var(--light)" stroke-width="1.3" fill="none"/></svg>
        info@velkoran.co.uk
      </li>
      <li>
        <svg viewBox="0 0 24 24" aria-hidden="true"><circle cx="12" cy="12" r="11" fill="var(--light)"/><g stroke="var(--charcoal)" stroke-width="1.4" fill="none"><circle cx="12" cy="12" r="6.5"/><ellipse cx="12" cy="12" rx="3" ry="6.5"/><path d="M5.5 12h13"/></g></svg>
        www.velkoran.co.uk
      </li>
    </ul>

    <div class="divider"></div>
    <address class="address">Milo Velkoran 18 Brindle Cope Lane<br>Waltham Cross,Herts,EN4 2QW</address>
  </section>

  <section class="card card--back" aria-label="Business card back">
    <div class="brand-name">VELKORAN</div>
    <p class="web">www.velkoran.co.uk</p>
  </section>

</main>
</body>
</html>
```